ultra-minimalist business card

front (black background, matte):

tarik b. hosseny
writer | photographer
get@tarikhosseny.com

back (white background, matte):

a picture speaks a thousand words;
a word draws a thousand pictures.

www.tarikhosseny.com

all text should be small (white or silver - as long as it shows against the black - on the front; black or gray - as long as it shows against the white - on the back).

feel free to get creative in terms of arrangement, alignment, and font type, but remember, the overall style is minimalist, so nothing too fancy, please.

thanks.

```html
<!DOCTYPE html>
<html lang="en">
<head>
<meta charset="utf-8">
<title>Tarik B. Hosseny — Business Card</title>
<link href="https://fonts.googleapis.com/css2?family=Nunito+Sans:wght@300;400;500&display=swap" rel="stylesheet">
<style>
  :root {
    --ink: #0a0b0b;
    --paper: #ffffff;
    --type-light: #ffffff;
    --type-dark: #111111;
  }
  * { margin: 0; padding: 0; box-sizing: border-box; }
  html, body {
    width: 1200px;
    height: 900px;
    overflow: hidden;
    background: var(--paper);
    font-family: "Nunito Sans", "Avenir Next", Arial, sans-serif;
  }
  .card {
    position: relative;
    width: 1200px;
    height: 900px;
  }
  .card-front {
    position: absolute;
    inset: 0 0 450px 0;
    background: var(--ink);
    color: var(--type-light);
  }
  .card-back {
    position: absolute;
    inset: 450px 0 0 0;
    background: var(--paper);
    color: var(--type-dark);
  }
  .line {
    position: absolute;
    left: 0;
    right: 0;
    text-align: center;
    white-space: nowrap;
    line-height: 1;
  }
  .name {
    top: 168px;
    font-size: 29px;
    font-weight: 500;
    text-transform: uppercase;
    letter-spacing: 25px;
    padding-left: 25px;
  }
  .roles {
    top: 219px;
    font-size: 31px;
    font-weight: 400;
    letter-spacing: 14px;
    padding-left: 14px;
  }
  .email {
    top: 262px;
    font-size: 31px;
    font-weight: 400;
    letter-spacing: 13px;
    padding-left: 13px;
  }
  .motto {
    top: 166px;
    font-size: 30px;
    font-weight: 400;
    letter-spacing: 3.5px;
    line-height: 41px;
  }
  .website {
    top: 355px;
    font-size: 29px;
    font-weight: 400;
    letter-spacing: 18px;
    padding-left: 18px;
  }
</style>
</head>
<body>
  <main class="card">
    <section class="card-front">
      <h1 class="line name">tarik b. hosseny</h1>
      <p class="line roles">writer | photographer</p>
      <p class="line email">get@tarikhosseny.com</p>
    </section>
    <section class="card-back">
      <p class="line motto">a picture speaks a thousand words;<br>a word draws a thousand pictures.</p>
      <p class="line website">www.tarikhosseny.com</p>
    </section>
  </main>
</body>
</html>
```